Business Card Design Project for Investment Fund

Veloria Capital Management is an emerging wealth management firm based in New Jersey. It offers superior investment returns to high net worth individuals and institutions by finding undervalued assets.
We recently selected a company logo which was inspired by the Tucana constellation. Beta Tucanae is a group of six stars, containing star cluster 47 Tucanae, rated the second brightest object in the sky.
Now we need a business card design. Since we are an investment firm, the design should project a sense of stability, growth and professionalism. The owner is interested in something simple yet striking, which of course is consistent with the logo.
Wealthy individuals, probably middle aged or older, in the US
Investment

```html
<!DOCTYPE html>
<html lang="en">
<head>
<meta charset="utf-8">
<title>Veloria Capital Management – Business Cards</title>
<link rel="stylesheet" href="https://fonts.googleapis.com/css2?family=Lato:ital,wght@0,400;0,700;1,400&display=swap">
<style>
  :root {
    --backdrop: #d9dadc;
    --navy-deep: #0a1560;
    --navy-bright: #1d4fd6;
    --brand-blue: #1237b8;
    --ink: #3a3d44;
    --ink-soft: #5b5f66;
    --rule: #8a8d93;
    --card-white: #f7f7f8;
    --card-grey: #e6e7ea;
    --on-dark: #e9ecf6;
  }
  * { margin: 0; padding: 0; box-sizing: border-box; }
  html, body { width: 1200px; height: 900px; overflow: hidden; }
  body {
    background: var(--backdrop);
    font-family: "Lato", Arial, sans-serif;
    position: relative;
  }
  .card {
    position: absolute;
    left: 240px;
    width: 720px;
    height: 400px;
    border-radius: 26px;
    overflow: hidden;
    box-shadow: 0 10px 30px rgba(0,0,0,0.18);
  }

  /* Back of card */
  .card-back {
    top: 40px;
    background: linear-gradient(135deg, var(--navy-deep) 0%, var(--brand-blue) 55%, var(--navy-bright) 100%);
    color: var(--on-dark);
  }
  .card-back .star-field {
    position: absolute;
    right: 0; top: 0;
    width: 100%; height: 100%;
    background: radial-gradient(ellipse at 78% 40%, rgba(255,255,255,0.10), rgba(255,255,255,0) 55%);
  }
  .card-back .brand {
    position: absolute;
    left: 0; right: 0; top: 150px;
    display: flex;
    align-items: center;
    justify-content: center;
    gap: 18px;
  }
  .card-back .brand-square {
    width: 54px; height: 54px;
    border-radius: 12px;
    background: rgba(255,255,255,0.14);
    border: 1.5px solid rgba(255,255,255,0.55);
  }
  .card-back .brand-name {
    font-size: 34px;
    font-weight: 700;
    letter-spacing: 0.5px;
    color: var(--on-dark);
  }
  .card-back .website {
    position: absolute;
    left: 0; right: 0; top: 262px;
    text-align: center;
    font-size: 17px;
    letter-spacing: 1px;
    color: var(--on-dark);
  }

  /* Front of card */
  .card-front {
    top: 470px;
    background: linear-gradient(180deg, var(--card-white) 0%, var(--card-grey) 100%);
    color: var(--ink);
  }
  .card-front .star-field {
    position: absolute;
    right: 0; top: 40px;
    width: 440px; height: 260px;
    background: radial-gradient(ellipse at 65% 45%, rgba(255,255,255,0.9), rgba(255,255,255,0) 65%);
  }
  .card-front .brand {
    position: absolute;
    left: 56px; top: 44px;
    display: flex;
    align-items: center;
    gap: 18px;
  }
  .card-front .brand-square {
    width: 84px; height: 84px;
    border-radius: 14px;
    background: linear-gradient(150deg, var(--brand-blue), var(--navy-deep));
  }
  .card-front .brand-name {
    font-size: 30px;
    font-weight: 700;
    color: var(--ink);
  }
  .card-front .holder {
    position: absolute;
    left: 56px; top: 204px;
    width: 300px;
    padding-bottom: 8px;
    border-bottom: 1.5px solid var(--rule);
  }
  .card-front .holder-name {
    font-size: 22px;
    font-style: italic;
    color: var(--brand-blue);
  }
  .card-front .holder-title {
    font-size: 14px;
    color: var(--ink-soft);
    margin-left: 4px;
  }
  .card-front .contact {
    position: absolute;
    right: 50px; top: 292px;
    width: 340px;
    padding-top: 6px;
    border-top: 1.5px solid var(--rule);
    font-size: 17px;
    line-height: 25px;
    color: var(--ink);
  }
  .card-front .contact-row {
    display: flex;
    align-items: center;
    gap: 16px;
  }
  .card-front .contact-row svg { flex: none; }
  .card-front .contact-row.address { padding-left: 0; }
</style>
</head>
<body>

  <section class="card card-back" aria-label="Business card back">
    <div class="star-field" role="img" aria-label="Faint compass-star constellation pattern"></div>
    <div class="brand">
      <span class="brand-square"></span>
      <span class="brand-name">Veloria Capital Management</span>
    </div>
    <p class="website">www.veloriacapmgmt.com</p>
  </section>

  <section class="card card-front" aria-label="Business card front">
    <div class="star-field" role="img" aria-label="Faint compass-star constellation pattern"></div>
    <div class="brand">
      <span class="brand-square"></span>
      <span class="brand-name">Veloria Capital Management</span>
    </div>

    <div class="holder">
      <span class="holder-name">Evan Harper</span>
      <span class="holder-title">• CEO</span>
    </div>

    <div class="contact">
      <div class="contact-row address">48 Harbor Ave. Newark, NJ 07102</div>
      <div class="contact-row">
        <svg width="16" height="16" viewBox="0 0 16 16" aria-hidden="true">
          <rect x="1" y="1" width="14" height="14" rx="2" fill="none" stroke="#1237b8" stroke-width="1.6"/>
          <rect x="3.5" y="3" width="4" height="10" rx="1" fill="#1237b8"/>
          <rect x="9" y="4" width="4" height="2" fill="#1237b8"/>
          <rect x="9" y="7.5" width="4" height="2" fill="#1237b8"/>
          <rect x="9" y="11" width="4" height="2" fill="#1237b8"/>
        </svg>
        <span>973-555-0142</span>
      </div>
      <div class="contact-row">
        <svg width="16" height="12" viewBox="0 0 16 12" aria-hidden="true">
          <rect x="0.8" y="0.8" width="14.4" height="10.4" fill="none" stroke="#1237b8" stroke-width="1.6"/>
          <path d="M1 1 L8 7 L15 1" fill="none" stroke="#1237b8" stroke-width="1.6"/>
        </svg>
        <span>eharper@veloriacapmgmt.com</span>
      </div>
    </div>
  </section>

</body>
</html>
```